Tovrimel Complete Stationery - Logo already designed

I already have the logo designed see attached. I need have a full set of stationary and business card designed for printing. I have attached an example of what I mean.

Please feel free to be creative. Also you can use the X in the logo by its self if you think it will work.

My details:

Name: Dorian Pelsett
Social media handles: @dorianpelsett
W: dorianpelsett.com
E: info@dorianpelsett.com
​P: 08 7349 5286
PO Box 3872, Wendlemore 6047
ABN 83 274 908 615

Target Market(s)

Anyone looking to be inspired.

Industry/Entity Type

Business

Font styles to use
Sans Serif

Colors
fbee3e
000000

Requirements
Must have
• My details:
• Name: Dorian Pelsett
• Social media handles: @dorianpelsett
• W: dorianpelsett.com
• E: info@dorianpelsett.com
• ​P: 08 7349 5286
• PO Box 3872, Wendlemore 6047
• ABN 83 274 908 615
Nice to have
• Something a little different
Should not have
• must not look tacky.

```html
<!DOCTYPE html>
<html lang="en">
<head>
<meta charset="UTF-8">
<title>Tovrimel Business Card</title>
<link rel="stylesheet" href="https://fonts.googleapis.com/css2?family=Roboto:wght@400;700;900&display=swap">
<style>
  :root {
    --backdrop: #1c1c1e;
    --brand-yellow: #fbee3e;
    --brand-gold: #f2c21a;
    --ink: #2a2a2a;
    --ink-soft: #3a3a3a;
    --card-black: #141414;
    --card-white: #ffffff;
    --wash: #fbf1c8;
  }
  * { margin: 0; padding: 0; box-sizing: border-box; }
  html, body {
    width: 1200px;
    height: 843px;
    overflow: hidden;
    background: var(--backdrop);
    font-family: "Roboto", Arial, sans-serif;
  }
  .stage {
    position: relative;
    width: 1200px;
    height: 843px;
  }
  .card {
    position: absolute;
    top: 273px;
    width: 520px;
    height: 297px;
    overflow: hidden;
    box-shadow: 0 14px 32px rgba(0,0,0,0.55);
  }
  /* Back of card */
  .card-back {
    left: 50px;
    background: linear-gradient(135deg, #202020 0%, var(--card-black) 60%, #0c0c0c 100%);
  }
  .card-back .wordmark {
    position: absolute;
    left: 0; right: 0;
    top: 104px;
    text-align: center;
    font-weight: 900;
    font-size: 64px;
    letter-spacing: 1px;
    text-transform: uppercase;
    color: var(--card-white);
  }
  .card-back .handle {
    position: absolute;
    left: 0; right: 0;
    top: 190px;
    text-align: center;
    font-weight: 700;
    font-size: 15px;
    letter-spacing: 0.5px;
    color: var(--brand-gold);
  }
  /* Front of card */
  .card-front {
    left: 630px;
    background: var(--card-white);
  }
  .card-front .wash {
    position: absolute;
    left: 0; top: 0;
    width: 250px;
    height: 297px;
    background: linear-gradient(110deg, var(--wash) 0%, #fdf6dc 60%, rgba(255,255,255,0) 100%);
  }
  .details {
    position: absolute;
    right: 26px;
    top: 48px;
    text-align: right;
    color: var(--ink-soft);
    font-size: 12.5px;
    line-height: 17px;
  }
  .details .person {
    font-weight: 700;
    font-size: 17px;
    line-height: 22px;
    color: var(--ink);
  }
  .card-front .wordmark {
    position: absolute;
    right: 26px;
    top: 112px;
    font-weight: 900;
    font-size: 60px;
    letter-spacing: 1px;
    text-transform: uppercase;
    color: var(--ink);
  }
  .contact {
    position: absolute;
    right: 26px;
    top: 208px;
    list-style: none;
    color: var(--ink-soft);
    font-size: 12.5px;
    line-height: 19px;
  }
  .contact li {
    display: flex;
    justify-content: flex-end;
    align-items: center;
    gap: 8px;
  }
  .contact svg {
    width: 12px;
    height: 12px;
    fill: var(--ink);
  }
</style>
</head>
<body>
<main class="stage">
  <section class="card card-back" aria-label="Business card back">
    <div class="wordmark">Tovrimel</div>
    <div class="handle">@dorianpelsett</div>
  </section>

  <section class="card card-front" aria-label="Business card front">
    <div class="wash" role="img" aria-label="Soft yellow wash where a large faint brand mark sits"></div>
    <div class="details">
      <p class="person">Dorian Pelsett</p>
      <p>PO Box 3872, Wendlemore 6047</p>
      <p>ABN 83 274 908 615</p>
    </div>
    <div class="wordmark">Tovrimel</div>
    <ul class="contact">
      <li>08 7349 5286
        <svg viewBox="0 0 24 24" aria-hidden="true"><path d="M6.6 10.8a15 15 0 0 0 6.6 6.6l2.2-2.2a1 1 0 0 1 1-.25 11.4 11.4 0 0 0 3.6.57 1 1 0 0 1 1 1V20a1 1 0 0 1-1 1A17 17 0 0 1 3 4a1 1 0 0 1 1-1h3.5a1 1 0 0 1 1 1c0 1.25.2 2.45.57 3.57a1 1 0 0 1-.25 1z"/></svg>
      </li>
      <li>info@dorianpelsett.com
        <svg viewBox="0 0 24 24" aria-hidden="true"><path d="M2 5h20v14H2z M2 5l10 8 10-8" fill="none" stroke="#2a2a2a" stroke-width="2.4"/></svg>
      </li>
      <li>dorianpelsett.com
        <svg viewBox="0 0 24 24" aria-hidden="true"><circle cx="12" cy="12" r="10"/></svg>
      </li>
    </ul>
  </section>
</main>
</body>
</html>
```